We are working on a book for our business you helped us design a logo for Title : Bright Path Forward:
Sub Title : Growing your venture while keeping your heart
Authors : Marcus Tolvane and Owen Brinks

we would like the book cover to be simple and complimentary to the logo but not exactly the same.

```html
<!DOCTYPE html>
<html lang="en">
<head>
<meta charset="utf-8">
<title>Bright Path Forward — Book Cover</title>
<link href="https://fonts.googleapis.com/css2?family=Anton&family=Oswald:wght@500;600&family=Roboto+Condensed:wght@700&display=swap" rel="stylesheet">
<style>
  :root {
    --backdrop: #ecebe7;
    --navy-light: #1f3a66;
    --navy-dark: #0d1f3f;
    --gold: #dcb65f;
    --gold-light: #f3dc95;
    --gold-deep: #b88a34;
    --badge-red: #e0262e;
    --white: #ffffff;
    --rule: #c9cfdc;
  }
  * { margin: 0; padding: 0; box-sizing: border-box; }
  html, body {
    width: 1200px; height: 1200px; overflow: hidden;
    background: var(--backdrop);
  }
  .book-cover {
    position: absolute;
    left: 220px; top: 50px;
    width: 760px; height: 1100px;
    background: radial-gradient(ellipse at 35% 25%, var(--navy-light), var(--navy-dark) 75%);
    border-top: 6px solid var(--gold);
    border-bottom: 6px solid var(--gold);
    overflow: hidden;
    box-shadow: 0 10px 30px rgba(0,0,0,0.25);
  }
  .title-badge {
    position: absolute;
    left: 130px; top: 80px;
    width: 260px; height: 260px;
    border-radius: 50%;
    background: var(--badge-red);
  }
  .title-lead {
    position: absolute;
    left: 80px; top: 120px;
    font-family: "Anton", sans-serif;
    color: var(--white);
    font-size: 96px;
    line-height: 0.92;
    letter-spacing: 1px;
    text-transform: uppercase;
  }
  .title-main {
    position: absolute;
    left: 40px; top: 300px;
    width: 680px; height: 420px;
  }
  .subtitle-block {
    position: absolute;
    left: 80px; top: 740px;
    width: 600px;
    text-align: center;
  }
  .subtitle-rule {
    height: 2px;
    background: var(--rule);
    margin: 0 30px;
  }
  .subtitle-text {
    font-family: "Roboto Condensed", sans-serif;
    font-weight: 700;
    color: var(--gold);
    font-size: 38px;
    line-height: 1.18;
    padding: 22px 0;
  }
  .authors {
    position: absolute;
    left: 0; right: 0; top: 935px;
    text-align: center;
    font-family: "Oswald", sans-serif;
    font-weight: 600;
    font-size: 56px;
    color: var(--gold);
    text-transform: uppercase;
    letter-spacing: -1px;
  }
  .authors .ampersand { color: var(--white); margin: 0 6px; }
</style>
</head>
<body>
  <main class="book-cover">
    <div class="title-badge"></div>
    <h1 class="title-lead">Bright<br>Path</h1>

    <svg class="title-main" viewBox="0 0 680 420" aria-label="Forward!">
      <defs>
        <linearGradient id="goldFill" x1="0" y1="0" x2="1" y2="1">
          <stop offset="0" stop-color="var(--gold-light)" style="stop-color:#f3dc95"/>
          <stop offset="0.5" stop-color="#dcb65f"/>
          <stop offset="1" stop-color="#b88a34"/>
        </linearGradient>
      </defs>
      <text x="0" y="380" font-family="Anton, sans-serif" font-size="330"
            textLength="680" lengthAdjust="spacingAndGlyphs"
            fill="url(#goldFill)">FORWARD!</text>
    </svg>

    <section class="subtitle-block">
      <div class="subtitle-rule"></div>
      <p class="subtitle-text">Growing your venture<br>while keeping your heart</p>
      <div class="subtitle-rule"></div>
    </section>

    <p class="authors">Marcus Tolvane<span class="ampersand">&amp;</span>Owen Brinks</p>
  </main>
</body>
</html>
```